Residential improvers, A Cozy Perch 2 Go *

Cozy Perch 2 Go is a real estate company specializing in turning unloved properties into improved, happy places to live. We specialize in thoughtfully-improved residential properties for buyers or renters. Our company needs a business card that reflects the renovated homes we create using green and Feng Shui principles,

Please disregard the images we submitted. We are looking for an abstract, sophisticated elegant design. No eggs in a nest ... nothing cute. The image can be soft.
Updates

Aloha (hello) all designers. We are a serious property investment/improvement company. We strive to be unique, renovating with style and elegance. Our business card must portray the same message. We thought the nest and flower might be "it" ... clearly it's not, once we saw what you submitted. Please revisit the brief as it was modified yesterday. Mahalo for your input! We look forward to hearing from all designers that have been invited.

Industry/Entity Type

Real Estate Development

Contact Information for Business Card

We will have separate business cards for
1) Corabeth Lindqvist 808-555-0173 corabeth@mailbrook.test
2) Marla Fenwright 808-555-0198 marlafenwright@mailbrook.test
** can we add the website later ... in the process of approval.
Investors * Renovators * Connectors

Font styles to use
Sans Serif

Colors
cadf82

Requirements
Must have
• a feng shui feel ... modern. Color - green with black print.
Nice to have
• A Cozy Perch 2 Go

```html
<!DOCTYPE html>
<html lang="en">
<head>
<meta charset="utf-8">
<title>A Cozy Perch 2 Go — Business Card</title>
<link rel="stylesheet" href="https://fonts.googleapis.com/css2?family=Cinzel:wght@600&family=Roboto:wght@400;500&display=swap">
<style>
  :root {
    --backdrop: #2a2a2a;
    --card-white: #ffffff;
    --brand-green: #cde087;
    --accent-green: #c9db7c;
    --ink-dark: #444444;
    --ink-grey: #6a6a6a;
    --wordmark-grey: #858585;
  }
  * { margin: 0; padding: 0; box-sizing: border-box; }
  html, body {
    width: 1200px;
    height: 1200px;
    overflow: hidden;
    background: var(--backdrop);
  }
  .card {
    position: absolute;
    left: 265px;
    width: 669px;
    height: 383px;
    border-radius: 30px;
    text-align: center;
  }
  .card--front { top: 196px; background: var(--card-white); }
  .card--back { top: 629px; background: var(--brand-green); }

  .person-name {
    position: absolute;
    top: 98px;
    width: 100%;
    font-family: "Cinzel", serif;
    font-weight: 600;
    font-size: 34px;
    line-height: 1;
    color: var(--accent-green);
    letter-spacing: 0.3px;
  }
  .person-title {
    position: absolute;
    top: 188px;
    width: 100%;
    font-family: "Roboto", sans-serif;
    font-weight: 500;
    font-size: 16.5px;
    letter-spacing: 0.6px;
    color: var(--accent-green);
  }
  .contact {
    position: absolute;
    top: 237px;
    width: 100%;
    font-family: "Roboto", sans-serif;
    font-size: 15.5px;
    line-height: 21.5px;
    letter-spacing: 1.2px;
    color: var(--ink-dark);
    list-style: none;
  }
  .contact__phone { font-weight: 500; }

  .company-name {
    position: absolute;
    top: 168px;
    width: 100%;
    font-family: "Roboto", sans-serif;
    font-weight: 400;
    font-size: 42px;
    line-height: 1;
    letter-spacing: 2px;
    color: var(--wordmark-grey);
  }
  .tagline {
    position: absolute;
    top: 322px;
    width: 100%;
    font-family: "Roboto", sans-serif;
    font-size: 15.5px;
    letter-spacing: 2px;
    color: var(--ink-grey);
  }
</style>
</head>
<body>
  <section class="card card--front">
    <h1 class="person-name">Corabeth Lindqvist</h1>
    <p class="person-title">FOUNDER &amp; CEO</p>
    <ul class="contact">
      <li class="contact__phone">808-555-0173</li>
      <li class="contact__email">corabeth@mailbrook.test</li>
      <li class="contact__web">www.acozyperch2go.test</li>
    </ul>
  </section>

  <section class="card card--back">
    <h2 class="company-name">A Cozy Perch 2 Go</h2>
    <p class="tagline">INVESTORS • RENOVATORS • CONNECTORS</p>
  </section>
</body>
</html>
```